The Pixel Tap Business card.

A Simple card with our Logo and contact information. To give to investors and other professionals.

We are a nerd themed bar.
our target market is young professionals age 21+ but the real purpose of this business card is to present to potential investors and other professionals with our contact information. as we are still looking for funding before we start up.

I am partial to green and my partner likes red we are open to iteration.

Target Market(s)

Investors

Industry/Entity Type

Business

Contact Information for Business Card

Martin Hale (225) 730-6192 kent.h4711@mailnest.test Glen Porter (225) 968-5037 glenp318@mailnest.test

Font styles to use
Serif

Requirements
Nice to have
• Keep it simple but not boring.
• Use the Logos but feel free to edit them to match theme/colors.
• Keep the back clean and use one of the Logos.

```html
<!DOCTYPE html>
<html lang="en">
<head>
<meta charset="utf-8">
<title>The Pixel Tap – Business Card</title>
<link href="https://fonts.googleapis.com/css2?family=Alegreya:wght@500;700&display=swap" rel="stylesheet">
<style>
  :root {
    --bg: #e6e9ee;
    --wine-dark: #3d0708;
    --wine: #6a1214;
    --wine-light: #7a1a1c;
    --gold: #d2ad62;
    --gold-light: #efd48d;
    --gold-text: #c79b55;
    --olive: #5d7d22;
    --olive-light: #6f8f2c;
  }
  html, body {
    margin: 0;
    width: 1200px;
    height: 675px;
    overflow: hidden;
    background: var(--bg);
    font-family: "Alegreya", Georgia, serif;
  }
  .stage {
    position: relative;
    width: 1200px;
    height: 675px;
    display: flex;
    align-items: center;
    justify-content: center;
    gap: 40px;
  }
  .card {
    position: relative;
    width: 520px;
    height: 297px;
    box-shadow: 0 10px 24px rgba(30, 40, 60, 0.25);
    overflow: hidden;
  }
  .card svg.card-art {
    position: absolute;
    inset: 0;
  }
  .brand {
    position: absolute;
    color: var(--gold-text);
    text-align: center;
    line-height: 1;
  }
  .brand-name {
    font-weight: 700;
    font-size: 34px;
    letter-spacing: 1px;
    text-transform: uppercase;
    display: flex;
    align-items: center;
    gap: 10px;
  }
  .brand-mark {
    width: 10px;
    height: 10px;
    border-radius: 50%;
    background: var(--gold-text);
  }
  .brand-tagline {
    font-weight: 700;
    font-size: 10px;
    letter-spacing: 1.5px;
    text-transform: uppercase;
    margin-top: 4px;
  }
  .card-back .brand {
    left: 0;
    right: 0;
    top: 128px;
    display: flex;
    flex-direction: column;
    align-items: center;
  }
  .card-front .brand {
    left: 48px;
    top: 150px;
    display: flex;
    flex-direction: column;
    align-items: center;
  }
  .contact {
    position: absolute;
    color: var(--gold-text);
    line-height: 1.25;
  }
  .contact-name {
    font-weight: 700;
    font-size: 19px;
  }
  .contact-line {
    font-weight: 500;
    font-size: 13px;
    padding-left: 10px;
  }
  .contact-primary { left: 62px; top: 218px; }
  .contact-secondary { left: 318px; top: 140px; }
</style>
</head>
<body>
<main class="stage">

  <section class="card card-back" aria-label="Business card back">
    <svg class="card-art" viewBox="0 0 520 297" width="520" height="297">
      <defs>
        <radialGradient id="wineBack" cx="0.55" cy="0.5" r="0.7">
          <stop offset="0" stop-color="var(--wine-light)"/>
          <stop offset="1" stop-color="var(--wine-dark)"/>
        </radialGradient>
        <linearGradient id="goldBack" x1="0" x2="1">
          <stop offset="0" stop-color="var(--gold)"/>
          <stop offset="0.5" stop-color="var(--gold-light)"/>
          <stop offset="1" stop-color="var(--gold)"/>
        </linearGradient>
      </defs>
      <rect class="panel-wine" width="520" height="297" fill="url(#wineBack)"/>
      <path class="panel-pattern" role="img" aria-label="Green panel with gold ornamental scroll pattern"
            d="M0 0 H520 V8 C380 16 200 40 0 44 Z" fill="var(--olive)"/>
      <path class="band-gold" d="M0 50 C200 46 380 20 520 12" stroke="url(#goldBack)" stroke-width="5" fill="none"/>
      <path class="panel-pattern" role="img" aria-label="Green panel with gold ornamental scroll pattern"
            d="M0 284 C160 280 330 258 520 238 V297 H0 Z" fill="var(--olive)"/>
      <path class="band-gold" d="M0 278 C160 274 330 252 520 232" stroke="url(#goldBack)" stroke-width="5" fill="none"/>
    </svg>
    <div class="brand">
      <div class="brand-name"><span class="brand-mark"></span>The Pixel Tap</div>
      <div class="brand-tagline">Lounge and Arcade</div>
    </div>
  </section>

  <section class="card card-front" aria-label="Business card front">
    <svg class="card-art" viewBox="0 0 520 297" width="520" height="297">
      <defs>
        <radialGradient id="wineFront" cx="0.5" cy="0.55" r="0.75">
          <stop offset="0" stop-color="var(--wine-light)"/>
          <stop offset="1" stop-color="var(--wine-dark)"/>
        </radialGradient>
        <linearGradient id="goldFront" x1="0" x2="1">
          <stop offset="0" stop-color="var(--gold)"/>
          <stop offset="0.5" stop-color="var(--gold-light)"/>
          <stop offset="1" stop-color="var(--gold)"/>
        </linearGradient>
      </defs>
      <rect class="panel-wine" width="520" height="297" fill="url(#wineFront)"/>
      <path class="panel-pattern" role="img" aria-label="Green panel with gold ornamental scroll pattern"
            d="M0 0 H520 V74 C400 78 250 84 120 90 C60 94 20 100 0 106 Z" fill="var(--olive)"/>
      <path class="band-gold" d="M0 114 C20 106 60 100 120 97 C250 91 400 86 520 82"
            stroke="url(#goldFront)" stroke-width="6" fill="none"/>
    </svg>
    <div class="brand">
      <div class="brand-name"><span class="brand-mark"></span>The Pixel Tap</div>
      <div class="brand-tagline">Lounge and Arcade</div>
    </div>
    <div class="contact contact-primary">
      <div class="contact-name">Martin Hale</div>
      <div class="contact-line">Phone: (225) 730-6192</div>
      <div class="contact-line">Email: kent.h4711@mailnest.test</div>
    </div>
    <div class="contact contact-secondary">
      <div class="contact-name">Glen Porter</div>
      <div class="contact-line">Phone: (225) 968-5037</div>
      <div class="contact-line">Email: glenp318@mailnest.test</div>
    </div>
  </section>

</main>
</body>
</html>
```